Baseball Teams Website

I need a website for our 2 baseball teams, which should include a page with the players and bios, a page with our schedule, a page with news and a page for donations to the team

```html
<!DOCTYPE html>
<html lang="en">
<head>
<meta charset="utf-8">
<title>Team Baseball</title>
<link href="https://fonts.googleapis.com/css2?family=Oswald:wght@500;600;700&family=Roboto:wght@400;500;700&display=swap" rel="stylesheet">
<style>
:root{
  --navy:#121a33;
  --navy-deep:#0b1124;
  --red:#d2213f;
  --ink:#1b1f2e;
  --muted:#555b6b;
  --line:#e3a3ae;
  --grey-row:#f1f1f3;
  --white:#ffffff;
}
*{box-sizing:border-box;margin:0;padding:0}
html,body{width:1200px;height:5188px;overflow:hidden}
body{font-family:"Roboto",Arial,sans-serif;color:var(--ink);background:var(--white);position:relative}
.heading{font-family:"Oswald",Arial,sans-serif;font-weight:600;text-transform:uppercase}
.btn{display:inline-block;background:var(--red);color:var(--white);font-family:"Oswald",Arial,sans-serif;font-weight:500;text-transform:uppercase;font-size:20px;letter-spacing:.5px;padding:14px 30px;line-height:1}
.section-title{font-family:"Oswald",Arial,sans-serif;font-weight:600;text-transform:uppercase;font-size:50px;text-align:center;color:var(--red);line-height:1}
.section-title.light{color:var(--white)}

/* header + hero */
.hero{position:absolute;left:0;top:0;width:1200px;height:688px;background:radial-gradient(ellipse at 70% 20%,#5a6c96 0%,#27365c 35%,#0d1430 80%)}
.site-header{position:absolute;left:0;top:0;width:1200px;height:88px;background:rgba(11,17,36,.9);display:flex;align-items:center;padding:0 176px}
.logo{font-family:"Oswald",Arial,sans-serif;font-weight:500;font-size:30px;color:var(--white);letter-spacing:1px}
.main-nav{margin-left:auto;display:flex;align-items:center;gap:34px}
.main-nav a{font-family:"Oswald",Arial,sans-serif;font-weight:500;font-size:17px;color:var(--white);text-transform:uppercase;text-decoration:none}
.main-nav .btn{font-size:18px;padding:14px 28px}
.hero-copy{position:absolute;left:160px;top:176px;width:460px}
.hero-copy h1{font-family:"Oswald",Arial,sans-serif;font-weight:700;font-size:58px;line-height:1.12;color:var(--white);text-transform:uppercase}
.hero-copy .btn{margin-top:26px;font-size:19px;padding:14px 24px}

/* about */
.about{position:absolute;left:0;top:688px;width:1200px;height:584px}
.about .section-title{margin-top:52px}
.about p{width:848px;margin:36px auto 0;text-align:center;font-size:18px;line-height:1.6;color:var(--ink)}
.about-media{position:absolute;top:240px;left:176px;display:flex;gap:32px}
.photo{position:relative}
.about-media .photo{width:408px;height:192px;background:linear-gradient(160deg,#7f9bc0,#2d3f63 60%,#3f6b3a)}
.play{position:absolute;left:50%;top:50%;width:72px;height:72px;margin:-36px 0 0 -36px;border:4px solid var(--white);border-radius:50%}
.play svg{position:absolute;left:22px;top:18px}
.about .btn{position:absolute;left:524px;top:460px}

/* players */
.players{position:absolute;left:0;top:1272px;width:1200px;height:728px;background:linear-gradient(180deg,#0f1936,#1f2d55 55%,#0f1936 88%);}
.players .section-title{margin-top:56px}
.player-row{position:absolute;left:180px;top:148px;display:flex;gap:60px}
.player-card{width:240px;text-align:center}
.player-card .photo{height:440px;background:linear-gradient(180deg,rgba(255,255,255,0) 0%,#9aa3b4 35%,#cfd3dc 70%,#8e96a8)}
.player-band{position:absolute;left:0;top:588px;width:1200px;height:140px;background:var(--white)}
.player-meta{position:absolute;top:620px;width:240px;text-align:center}
.player-meta h3{font-family:"Oswald",Arial,sans-serif;font-weight:600;font-size:26px;text-transform:uppercase;color:var(--ink)}
.player-meta a{display:inline-block;margin-top:8px;font-family:"Oswald",Arial,sans-serif;font-weight:600;font-size:17px;color:var(--red);text-decoration:underline;text-transform:uppercase}
.arrow{position:absolute;top:332px}

/* schedule */
.schedule{position:absolute;left:0;top:2000px;width:1200px;height:1380px}
.schedule .section-title{margin-top:56px}
.schedule-table{position:absolute;left:176px;top:140px;width:848px;border-collapse:collapse;border:2px solid var(--line)}
.schedule-table th{background:var(--navy);color:var(--white);font-family:"Oswald",Arial,sans-serif;font-weight:500;font-size:15px;text-transform:uppercase;height:72px;text-align:left;padding:0 20px;border-right:1px solid #2c3553}
.schedule-table td{height:180px;vertical-align:top;padding:34px 20px 0;font-size:15px;line-height:1.5;border-right:1px solid #d7d9df;color:var(--ink)}
.schedule-table tr:nth-child(even) td{background:var(--grey-row)}
.schedule-table td strong{display:block;font-weight:700}
.date-cell{white-space:nowrap;font-weight:500}
.date-cell svg{vertical-align:-2px;margin-right:6px}
.schedule .btn.calendar{position:absolute;left:526px;top:976px}
.countdown-title{position:absolute;left:0;top:1112px;width:1200px;text-align:center;font-family:"Oswald",Arial,sans-serif;font-weight:600;font-size:32px;color:var(--red);text-transform:uppercase}
.countdown{position:absolute;left:256px;top:1180px;width:688px;height:160px;border:2px solid var(--line);display:flex;justify-content:center;align-items:center;gap:40px}
.unit{text-align:center;width:90px}
.unit b{display:block;font-family:"Oswald",Arial,sans-serif;font-weight:600;font-size:46px;color:var(--red);line-height:1}
.unit span{display:block;margin-top:10px;font-size:13px;color:var(--muted);text-transform:uppercase;letter-spacing:1px}
.sep{font-family:"Oswald",Arial,sans-serif;font-size:40px;color:var(--ink);margin-top:-24px}

/* blog */
.blog{position:absolute;left:0;top:3400px;width:1200px;height:820px;background:linear-gradient(180deg,#101a38,#2a3a62 50%,#121b3a)}
.blog .section-title{margin-top:52px}
.blog .photo{position:absolute;background:linear-gradient(160deg,#8fa6c6,#39507a 55%,#4c7a43)}
.blog-text{position:absolute;background:var(--white);padding:22px 18px}
.blog-meta{display:flex;gap:14px;font-size:13px;color:var(--ink);align-items:center}
.blog-meta svg{vertical-align:-2px;margin-right:4px}
.blog-text p{margin-top:14px;font-size:13px;line-height:1.55;color:var(--muted)}
.blog-text .btn{margin-top:18px;font-size:14px;padding:10px 16px}

/* promo */
.promo{position:absolute;left:0;top:4220px;width:1200px;height:560px;background:var(--white)}
.promo .photo{position:absolute;left:0;top:60px;width:600px;height:500px;background:radial-gradient(ellipse at 45% 55%,#b9bec9 0%,#7c8495 40%,rgba(255,255,255,0) 72%)}
.promo-copy{position:absolute;left:624px;top:160px;width:440px;text-align:center}
.promo-copy h2{font-family:"Oswald",Arial,sans-serif;font-weight:700;font-size:46px;line-height:1.2;text-transform:uppercase;color:var(--ink)}
.promo-copy p{margin-top:22px;font-size:18px;line-height:1.55;color:var(--ink)}
.promo-copy .btn{margin-top:30px}

/* footer */
.site-footer{position:absolute;left:0;top:4780px;width:1200px;height:328px;background:var(--navy-deep)}
.contact-box{position:absolute;left:176px;top:100px;width:848px;height:168px;border:2px solid var(--red);display:flex}
.contact-col{flex:1;padding:34px 30px;color:var(--white);border-right:2px solid var(--red)}
.contact-col:last-child{border-right:0;text-align:center}
.contact-col h4{font-family:"Roboto",Arial,sans-serif;font-weight:700;font-size:20px;display:flex;align-items:center;gap:12px}
.contact-col:last-child h4{justify-content:center}
.contact-col p{margin-top:10px;padding-left:32px;font-size:16px;line-height:1.5}
.contact-col .phone{font-size:24px;font-weight:500}
.social{display:flex;justify-content:center;gap:18px;margin-top:22px}
.social span{width:40px;height:40px;border-radius:50%;background:var(--white)}
.social span:nth-child(2){background:var(--red)}
.bottom-bar{position:absolute;left:0;top:5108px;width:1200px;height:80px;background:var(--red);display:flex;align-items:center;padding:0 176px;color:var(--white);font-size:17px}
.bottom-bar nav{margin-left:auto;display:flex;gap:36px}
</style>
</head>
<body>

<section class="hero" role="img" aria-label="Night stadium photograph with a batter and catcher at home plate">
  <header class="site-header">
    <div class="logo">LOGO HERE</div>
    <nav class="main-nav">
      <a href="#">Home</a>
      <a href="#">Players &amp; Bios</a>
      <a href="#">Schedule</a>
      <a href="#">News</a>
      <a href="#">About</a>
      <a class="btn" href="#">Donate</a>
    </nav>
  </header>
  <div class="hero-copy">
    <h1>Meet all the heros from field</h1>
    <a class="btn" href="#">Read more</a>
  </div>
</section>

<section class="about">
  <h2 class="section-title">About us</h2>
  <p>Lorem Ipsum is simply dummy text of the printing and typesetting industry. Lorem Ipsum has been the industry's standard dummy text ever since the 1500s, when an unknown printer took a galley of type and scrambled it to make a type specimen book.</p>
  <div class="about-media">
    <div class="photo" role="img" aria-label="Batter swinging in a lit stadium"></div>
    <div class="photo" role="img" aria-label="Video still of players on the diamond">
      <span class="play"><svg width="28" height="32" viewBox="0 0 28 32"><path d="M2 2 L26 16 L2 30 Z" fill="#d2213f"/></svg></span>
    </div>
  </div>
  <a class="btn" href="#">View more</a>
</section>

<section class="players">
  <h2 class="section-title light">Player profiles</h2>
  <div class="player-band"></div>
  <div class="player-row">
    <div class="player-card"><div class="photo" role="img" aria-label="Player portrait holding a bat"></div></div>
    <div class="player-card"><div class="photo" role="img" aria-label="Player portrait holding a bat"></div></div>
    <div class="player-card"><div class="photo" role="img" aria-label="Player portrait holding a bat"></div></div>
  </div>
  <div class="player-meta" style="left:180px"><h3>Dale Grover</h3><a href="#">View bio</a></div>
  <div class="player-meta" style="left:480px"><h3>Dale Grover</h3><a href="#">View bio</a></div>
  <div class="player-meta" style="left:780px"><h3>Dale Grover</h3><a href="#">View bio</a></div>
  <svg class="arrow" style="left:72px" width="28" height="44" viewBox="0 0 28 44"><path d="M24 4 L6 22 L24 40" fill="none" stroke="#fff" stroke-width="6"/></svg>
  <svg class="arrow" style="left:1100px" width="28" height="44" viewBox="0 0 28 44"><path d="M4 4 L22 22 L4 40" fill="none" stroke="#fff" stroke-width="6"/></svg>
</section>

<section class="schedule">
  <h2 class="section-title">Our schedule</h2>
  <table class="schedule-table">
    <colgroup><col style="width:104px"><col style="width:208px"><col style="width:208px"><col style="width:176px"><col style="width:152px"></colgroup>
    <thead><tr><th>Date</th><th>Opponent / Event</th><th>Venue / Location</th><th>Time(ET) / Score</th><th>Notes</th></tr></thead>
    <tbody>
      <tr><td class="date-cell"><svg width="14" height="14" viewBox="0 0 14 14"><rect x="1" y="2" width="12" height="11" fill="none" stroke="#d2213f" stroke-width="2"/><rect x="1" y="2" width="12" height="4" fill="#d2213f"/></svg>JUL 30</td><td><strong>Lorem Ipsum</strong>Lorem ipsum dolor sit amet, consectetur adipiscing.</td><td><strong>Lorem Ipsum</strong>Lorem ipsum dolor sit amet, consectetur.</td><td><strong>W, 1-2</strong></td><td>Lorem ipsum dolor sit amet, consectetur</td></tr>
      <tr><td class="date-cell"><svg width="14" height="14" viewBox="0 0 14 14"><rect x="1" y="2" width="12" height="11" fill="none" stroke="#d2213f" stroke-width="2"/><rect x="1" y="2" width="12" height="4" fill="#d2213f"/></svg>JUL 30</td><td><strong>Lorem Ipsum</strong>Lorem ipsum dolor sit amet, consectetur adipiscing.</td><td><strong>Lorem Ipsum</strong>Lorem ipsum dolor sit amet, consectetur.</td><td><strong>W, 1-2</strong></td><td>Lorem ipsum dolor sit amet, consectetur</td></tr>
      <tr><td class="date-cell"><svg width="14" height="14" viewBox="0 0 14 14"><rect x="1" y="2" width="12" height="11" fill="none" stroke="#d2213f" stroke-width="2"/><rect x="1" y="2" width="12" height="4" fill="#d2213f"/></svg>JUL 30</td><td><strong>Lorem Ipsum</strong>Lorem ipsum dolor sit amet, consectetur adipiscing.</td><td><strong>Lorem Ipsum</strong>Lorem ipsum dolor sit amet, consectetur.</td><td><strong>W, 1-2</strong></td><td>Lorem ipsum dolor sit amet, consectetur</td></tr>
      <tr><td class="date-cell"><svg width="14" height="14" viewBox="0 0 14 14"><rect x="1" y="2" width="12" height="11" fill="none" stroke="#d2213f" stroke-width="2"/><rect x="1" y="2" width="12" height="4" fill="#d2213f"/></svg>JUL 30</td><td><strong>Lorem Ipsum</strong>Lorem ipsum dolor sit amet, consectetur adipiscing.</td><td><strong>Lorem Ipsum</strong>Lorem ipsum dolor sit amet, consectetur.</td><td><strong>W, 1-2</strong></td><td>Lorem ipsum dolor sit amet, consectetur</td></tr>
    </tbody>
  </table>
  <a class="btn calendar" href="#">Calender</a>
  <h3 class="countdown-title">Upcoming game coming soon</h3>
  <div class="countdown">
    <div class="unit"><b>02</b><span>Days</span></div><div class="sep">:</div>
    <div class="unit"><b>74</b><span>Hours</span></div><div class="sep">:</div>
    <div class="unit"><b>56</b><span>Minutes</span></div><div class="sep">:</div>
    <div class="unit"><b>55</b><span>Minutes</span></div>
  </div>
</section>

<section class="blog">
  <h2 class="section-title light">Blog</h2>
  <div class="photo" style="left:176px;top:140px;width:204px;height:288px" role="img" aria-label="Batter and catcher at the plate"></div>
  <div class="blog-text" style="left:380px;top:140px;width:220px;height:288px">
    <div class="blog-meta"><span><svg width="12" height="12" viewBox="0 0 14 14"><rect x="1" y="2" width="12" height="11" fill="#d2213f"/></svg>21/12/2021</span><span><svg width="12" height="12" viewBox="0 0 14 14"><circle cx="7" cy="7" r="5.5" fill="none" stroke="#d2213f" stroke-width="2"/><path d="M7 4v3.5h2.5" stroke="#d2213f" stroke-width="1.6" fill="none"/></svg>12:43 AM</span></div>
    <p>Lorem Ipsum is simply dummy text of the printing and typesetting industry. Lorem Ipsum has been the industry's specimen book</p>
    <a class="btn" href="#">Read more</a>
  </div>
  <div class="photo" style="left:616px;top:140px;width:408px;height:288px" role="img" aria-label="Video still of a play on the infield">
    <span class="play"><svg width="28" height="32" viewBox="0 0 28 32"><path d="M2 2 L26 16 L2 30 Z" fill="#fff"/></svg></span>
  </div>
  <div class="photo" style="left:176px;top:440px;width:408px;height:292px" role="img" aria-label="Video still of a packed stadium">
    <span class="play"><svg width="28" height="32" viewBox="0 0 28 32"><path d="M2 2 L26 16 L2 30 Z" fill="#fff"/></svg></span>
  </div>
  <div class="blog-text" style="left:600px;top:440px;width:220px;height:292px">
    <div class="blog-meta"><span><svg width="12" height="12" viewBox="0 0 14 14"><rect x="1" y="2" width="12" height="11" fill="#d2213f"/></svg>21/12/2021</span><span><svg width="12" height="12" viewBox="0 0 14 14"><circle cx="7" cy="7" r="5.5" fill="none" stroke="#d2213f" stroke-width="2"/><path d="M7 4v3.5h2.5" stroke="#d2213f" stroke-width="1.6" fill="none"/></svg>12:43 AM</span></div>
    <p>Lorem Ipsum is simply dummy text of the printing and typesetting industry. Lorem Ipsum has been the industry's specimen book</p>
    <a class="btn" href="#">Read more</a>
  </div>
  <div class="photo" style="left:820px;top:440px;width:204px;height:292px" role="img" aria-label="Fielder in the stands"></div>
  <svg class="arrow" style="position:absolute;left:72px;top:390px" width="28" height="44" viewBox="0 0 28 44"><path d="M24 4 L6 22 L24 40" fill="none" stroke="#fff" stroke-width="6"/></svg>
  <svg class="arrow" style="position:absolute;left:1100px;top:390px" width="28" height="44" viewBox="0 0 28 44"><path d="M4 4 L22 22 L4 40" fill="none" stroke="#fff" stroke-width="6"/></svg>
</section>

<section class="promo">
  <div class="photo" role="img" aria-label="Batter mid-swing cut out on white"></div>
  <div class="promo-copy">
    <h2>Lorem ipsum is simply dummy and typesetting</h2>
    <p>Lorem Ipsum is simply dummy text of the printing and typesetting industry. Lorem Ipsum has been the industry's known printer took a galley of type and scrambled</p>
    <a class="btn" href="#">Donate</a>
  </div>
</section>

<footer class="site-footer">
  <div class="contact-box">
    <div class="contact-col">
      <h4><svg width="20" height="24" viewBox="0 0 20 24"><path d="M10 1a8 8 0 0 0-8 8c0 6 8 14 8 14s8-8 8-14a8 8 0 0 0-8-8z" fill="#fff"/><circle cx="10" cy="9" r="3" fill="#0b1124"/></svg>Address</h4>
      <p>123 lorem is simply dummy text of theprintin</p>
    </div>
    <div class="contact-col">
      <h4><svg width="20" height="20" viewBox="0 0 20 20"><path d="M4 1l4 4-2 3c1 3 3 5 6 6l3-2 4 4-3 3C8 19 1 12 1 4z" fill="#fff"/></svg>Need any help?</h4>
      <p class="phone">(123) 4567 8913</p>
    </div>
    <div class="contact-col">
      <h4>Follow us</h4>
      <div class="social"><span></span><span></span><span></span></div>
    </div>
  </div>
  <div class="bottom-bar" style="top:328px;position:absolute"></div>
</footer>
<div class="bottom-bar">
  <span>© 2022 All rights reserved</span>
  <nav><span>Privacy</span><span>Terms &amp; Conditions</span></nav>
</div>

</body>
</html>
```